Want to go online this week, rush project, everything is there, just make it pretty

I need a pretty html5/css template for a already made site. Please do not rearrange anything unless you feel you can simplify the design. I have a raw site. Please play with the site by making an account with coupon code BRAMBLEPASS for free signup. Log in, log out, download as many designs as you can, then log in and log out. See everything cause it's brand new and I need it neat and pretty over the next few days if not sooner. So, after all that, the site is http://StitchloomPatternWorks.example
Updates

Project Deadline Extended
Reason: Extending until the 30th to give more time.

Is anyone working on something to submit? If you have something please submit asap as I will be closing this Sat night or Sunday morning

Industry/Entity Type

Online

Coding

Coded - Design and coding required

```html
<!DOCTYPE html>
<html lang="en">
<head>
<meta charset="utf-8">
<title>Embroidery Design Sets</title>
<link rel="stylesheet" href="https://fonts.googleapis.com/css2?family=Fira+Sans+Extra+Condensed:ital,wght@0,400;0,500;0,700;1,400&display=swap">
<style>
  :root {
    --page-bg: #ececec;
    --card-bg: #fbfbfb;
    --card-edge: #dcdcdc;
    --ink: #1c1c1c;
    --ink-soft: #3a3a3a;
    --muted: #7a7a7a;
    --chip-bg: #eaa6d0;
    --chip-ink: #7d1652;
    --btn-top: #cf3b8e;
    --btn-bottom: #a3155f;
    --footer-bg: #e2e2e2;
    --footer-ink: #8a8a8a;
  }
  * { box-sizing: border-box; margin: 0; padding: 0; }
  html, body { width: 1038px; height: 1200px; overflow: hidden; }
  body {
    position: relative;
    background: var(--page-bg);
    font-family: "Fira Sans Extra Condensed", "Arial Narrow", sans-serif;
    color: var(--ink);
  }
  .design-grid {
    position: absolute;
    left: 131px; top: 47px;
    display: grid;
    grid-template-columns: repeat(3, 245px);
    grid-template-rows: repeat(3, 310px);
    column-gap: 20px;
    row-gap: 18px;
  }
  .design-card {
    position: relative;
    background: linear-gradient(#ffffff, var(--card-bg));
    border: 1px solid var(--card-edge);
    box-shadow: 0 1px 2px rgba(0,0,0,.08);
  }
  .design-card__image { position: absolute; top: 6px; }
  .plume .design-card__image { left: 5px; width: 200px; height: 170px;
    background: radial-gradient(ellipse at 50% 45%, #c7cdf0 0%, #eef0fa 40%, #fafafa 75%); }
  .stroll .design-card__image { left: 38px; width: 160px; height: 180px;
    background: radial-gradient(ellipse at 50% 50%, #d7bde6 0%, #eee6f4 45%, #f5f3fa 80%); }
  .night .design-card__image { left: 8px; width: 206px; height: 167px;
    background: radial-gradient(ellipse at 50% 50%, #6d5bb0 0%, #c7b9d8 40%, #f6eef3 78%); }
  .design-card__title {
    position: absolute; left: 13px; top: 190px;
    font-size: 19px; font-weight: 700; letter-spacing: -.2px; white-space: nowrap;
  }
  .design-card__categories {
    position: absolute; left: 13px; top: 213px;
    font-size: 7.5px; color: var(--ink-soft); white-space: nowrap;
  }
  .design-card__categories b { font-weight: 700; color: var(--ink); }
  .design-card__meta {
    position: absolute; left: 14px; top: 231px;
    font-size: 13px; line-height: 15px; color: var(--ink);
  }
  .design-card__formats {
    position: absolute; left: 131px; top: 231px; width: 108px;
    font-size: 7.5px; color: var(--ink-soft);
  }
  .format-list { display: flex; flex-wrap: wrap; gap: 3px; margin-top: 6px; }
  .format-chip {
    width: 18px; height: 11px; line-height: 11px;
    background: var(--chip-bg); color: var(--chip-ink);
    font-size: 7px; text-align: center;
  }
  .view-set {
    position: absolute; left: 12px; top: 273px;
    width: 86px; height: 23px;
    display: flex; align-items: center; justify-content: center; gap: 8px;
    background: linear-gradient(var(--btn-top), var(--btn-bottom));
    border-radius: 4px;
    color: #fff; font-size: 12.5px; font-weight: 500; text-decoration: none;
  }
  .design-card__date {
    position: absolute; left: 131px; top: 277px;
    font-size: 10px; line-height: 11px; color: var(--ink-soft);
  }
  .design-card__date b { font-weight: 700; color: var(--ink); }
  .pager-status {
    position: absolute; left: 158px; top: 1052px;
    font-size: 18px; color: var(--muted);
  }
  .pager-next {
    position: absolute; left: 820px; top: 1055px;
    font-size: 13px; color: var(--muted); text-decoration: none;
  }
  .pager-next span { margin-left: 6px; font-size: 9px; }
  .site-footer {
    position: absolute; left: 0; top: 1129px; width: 1038px; height: 71px;
    background: var(--footer-bg);
    padding: 18px 0 0 158px;
    font-size: 9.5px; line-height: 14px; font-style: italic; color: var(--footer-ink);
  }
</style>
</head>
<body>
<main class="design-grid">
  <article class="design-card plume">
    <div class="design-card__image" role="img" aria-label="Embroidered blue feather with red stitching"></div>
    <h2 class="design-card__title">Soft As A Plume</h2>
    <p class="design-card__categories">Categories: <b>Filled Design, Red Work, Objects &amp; Things</b></p>
    <p class="design-card__meta">10 Designs<br>All Fit the 4x4 Hoop</p>
    <div class="design-card__formats">Download now, select your format:
      <div class="format-list"><span class="format-chip">ART</span><span class="format-chip">DST</span><span class="format-chip">EXP</span><span class="format-chip">HUS</span><span class="format-chip">JEF</span><span class="format-chip">PCS</span><span class="format-chip">PES</span><span class="format-chip">SEW</span><span class="format-chip">XIP</span><span class="format-chip">XXX</span></div>
    </div>
    <a class="view-set" href="#"><svg width="12" height="8" viewBox="0 0 12 8"><path d="M0 4C2 0.5 10 0.5 12 4C10 7.5 2 7.5 0 4Z" fill="#fff"/><circle cx="6" cy="4" r="1.8" fill="#b0206c"/></svg>View Set</a>
    <p class="design-card__date">Added/Updated:<br><b>October 08, 2014</b></p>
  </article>
  <article class="design-card stroll">
    <div class="design-card__image" role="img" aria-label="Embroidered girl in a purple dress walking a small dog"></div>
    <h2 class="design-card__title">Morning Stroll Out</h2>
    <p class="design-card__categories">Categories: <b>Filled Design, Dog, Girls, Animal</b></p>
    <p class="design-card__meta">10 Designs<br>All Fit the 4x4 Hoop</p>
    <div class="design-card__formats">Download now, select your format:
      <div class="format-list"><span class="format-chip">ART</span><span class="format-chip">DST</span><span class="format-chip">EXP</span><span class="format-chip">HUS</span><span class="format-chip">JEF</span><span class="format-chip">PCS</span><span class="format-chip">PES</span><span class="format-chip">SEW</span><span class="format-chip">XIP</span><span class="format-chip">XXX</span></div>
    </div>
    <a class="view-set" href="#"><svg width="12" height="8" viewBox="0 0 12 8"><path d="M0 4C2 0.5 10 0.5 12 4C10 7.5 2 7.5 0 4Z" fill="#fff"/><circle cx="6" cy="4" r="1.8" fill="#b0206c"/></svg>View Set</a>
    <p class="design-card__date">Added/Updated:<br><b>August 31, 2014</b></p>
  </article>
  <article class="design-card night">
    <div class="design-card__image" role="img" aria-label="Embroidered owl in a witch hat riding a broom"></div>
    <h2 class="design-card__title">Who Goes There</h2>
    <p class="design-card__categories">Categories: <b>Filled Design, Owl, Halloween, Animal</b></p>
    <p class="design-card__meta">10 Designs<br>All Fit the 4x4 Hoop</p>
    <div class="design-card__formats">Download now, select your format:
      <div class="format-list"><span class="format-chip">ART</span><span class="format-chip">DST</span><span class="format-chip">EXP</span><span class="format-chip">HUS</span><span class="format-chip">JEF</span><span class="format-chip">PCS</span><span class="format-chip">PES</span><span class="format-chip">SEW</span><span class="format-chip">XIP</span><span class="format-chip">XXX</span></div>
    </div>
    <a class="view-set" href="#"><svg width="12" height="8" viewBox="0 0 12 8"><path d="M0 4C2 0.5 10 0.5 12 4C10 7.5 2 7.5 0 4Z" fill="#fff"/><circle cx="6" cy="4" r="1.8" fill="#b0206c"/></svg>View Set</a>
    <p class="design-card__date">Added/Updated:<br><b>September 20, 2014</b></p>
  </article>

  <article class="design-card plume">
    <div class="design-card__image" role="img" aria-label="Embroidered blue feather with red stitching"></div>
    <h2 class="design-card__title">Soft As A Plume</h2>
    <p class="design-card__categories">Categories: <b>Filled Design, Red Work, Objects &amp; Things</b></p>
    <p class="design-card__meta">10 Designs<br>All Fit the 4x4 Hoop</p>
    <div class="design-card__formats">Download now, select your format:
      <div class="format-list"><span class="format-chip">ART</span><span class="format-chip">DST</span><span class="format-chip">EXP</span><span class="format-chip">HUS</span><span class="format-chip">JEF</span><span class="format-chip">PCS</span><span class="format-chip">PES</span><span class="format-chip">SEW</span><span class="format-chip">XIP</span><span class="format-chip">XXX</span></div>
    </div>
    <a class="view-set" href="#"><svg width="12" height="8" viewBox="0 0 12 8"><path d="M0 4C2 0.5 10 0.5 12 4C10 7.5 2 7.5 0 4Z" fill="#fff"/><circle cx="6" cy="4" r="1.8" fill="#b0206c"/></svg>View Set</a>
    <p class="design-card__date">Added/Updated:<br><b>October 08, 2014</b></p>
  </article>
  <article class="design-card stroll">
    <div class="design-card__image" role="img" aria-label="Embroidered girl in a purple dress walking a small dog"></div>
    <h2 class="design-card__title">Morning Stroll Out</h2>
    <p class="design-card__categories">Categories: <b>Filled Design, Dog, Girls, Animal</b></p>
    <p class="design-card__meta">10 Designs<br>All Fit the 4x4 Hoop</p>
    <div class="design-card__formats">Download now, select your format:
      <div class="format-list"><span class="format-chip">ART</span><span class="format-chip">DST</span><span class="format-chip">EXP</span><span class="format-chip">HUS</span><span class="format-chip">JEF</span><span class="format-chip">PCS</span><span class="format-chip">PES</span><span class="format-chip">SEW</span><span class="format-chip">XIP</span><span class="format-chip">XXX</span></div>
    </div>
    <a class="view-set" href="#"><svg width="12" height="8" viewBox="0 0 12 8"><path d="M0 4C2 0.5 10 0.5 12 4C10 7.5 2 7.5 0 4Z" fill="#fff"/><circle cx="6" cy="4" r="1.8" fill="#b0206c"/></svg>View Set</a>
    <p class="design-card__date">Added/Updated:<br><b>August 31, 2014</b></p>
  </article>
  <article class="design-card night">
    <div class="design-card__image" role="img" aria-label="Embroidered owl in a witch hat riding a broom"></div>
    <h2 class="design-card__title">Who Goes There</h2>
    <p class="design-card__categories">Categories: <b>Filled Design, Owl, Halloween, Animal</b></p>
    <p class="design-card__meta">10 Designs<br>All Fit the 4x4 Hoop</p>
    <div class="design-card__formats">Download now, select your format:
      <div class="format-list"><span class="format-chip">ART</span><span class="format-chip">DST</span><span class="format-chip">EXP</span><span class="format-chip">HUS</span><span class="format-chip">JEF</span><span class="format-chip">PCS</span><span class="format-chip">PES</span><span class="format-chip">SEW</span><span class="format-chip">XIP</span><span class="format-chip">XXX</span></div>
    </div>
    <a class="view-set" href="#"><svg width="12" height="8" viewBox="0 0 12 8"><path d="M0 4C2 0.5 10 0.5 12 4C10 7.5 2 7.5 0 4Z" fill="#fff"/><circle cx="6" cy="4" r="1.8" fill="#b0206c"/></svg>View Set</a>
    <p class="design-card__date">Added/Updated:<br><b>September 20, 2014</b></p>
  </article>

  <article class="design-card plume">
    <div class="design-card__image" role="img" aria-label="Embroidered blue feather with red stitching"></div>
    <h2 class="design-card__title">Soft As A Plume</h2>
    <p class="design-card__categories">Categories: <b>Filled Design, Red Work, Objects &amp; Things</b></p>
    <p class="design-card__meta">10 Designs<br>All Fit the 4x4 Hoop</p>
    <div class="design-card__formats">Download now, select your format:
      <div class="format-list"><span class="format-chip">ART</span><span class="format-chip">DST</span><span class="format-chip">EXP</span><span class="format-chip">HUS</span><span class="format-chip">JEF</span><span class="format-chip">PCS</span><span class="format-chip">PES</span><span class="format-chip">SEW</span><span class="format-chip">XIP</span><span class="format-chip">XXX</span></div>
    </div>
    <a class="view-set" href="#"><svg width="12" height="8" viewBox="0 0 12 8"><path d="M0 4C2 0.5 10 0.5 12 4C10 7.5 2 7.5 0 4Z" fill="#fff"/><circle cx="6" cy="4" r="1.8" fill="#b0206c"/></svg>View Set</a>
    <p class="design-card__date">Added/Updated:<br><b>October 08, 2014</b></p>
  </article>
  <article class="design-card stroll">
    <div class="design-card__image" role="img" aria-label="Embroidered girl in a purple dress walking a small dog"></div>
    <h2 class="design-card__title">Morning Stroll Out</h2>
    <p class="design-card__categories">Categories: <b>Filled Design, Dog, Girls, Animal</b></p>
    <p class="design-card__meta">10 Designs<br>All Fit the 4x4 Hoop</p>
    <div class="design-card__formats">Download now, select your format:
      <div class="format-list"><span class="format-chip">ART</span><span class="format-chip">DST</span><span class="format-chip">EXP</span><span class="format-chip">HUS</span><span class="format-chip">JEF</span><span class="format-chip">PCS</span><span class="format-chip">PES</span><span class="format-chip">SEW</span><span class="format-chip">XIP</span><span class="format-chip">XXX</span></div>
    </div>
    <a class="view-set" href="#"><svg width="12" height="8" viewBox="0 0 12 8"><path d="M0 4C2 0.5 10 0.5 12 4C10 7.5 2 7.5 0 4Z" fill="#fff"/><circle cx="6" cy="4" r="1.8" fill="#b0206c"/></svg>View Set</a>
    <p class="design-card__date">Added/Updated:<br><b>August 31, 2014</b></p>
  </article>
  <article class="design-card night">
    <div class="design-card__image" role="img" aria-label="Embroidered owl in a witch hat riding a broom"></div>
    <h2 class="design-card__title">Who Goes There</h2>
    <p class="design-card__categories">Categories: <b>Filled Design, Owl, Halloween, Animal</b></p>
    <p class="design-card__meta">10 Designs<br>All Fit the 4x4 Hoop</p>
    <div class="design-card__formats">Download now, select your format:
      <div class="format-list"><span class="format-chip">ART</span><span class="format-chip">DST</span><span class="format-chip">EXP</span><span class="format-chip">HUS</span><span class="format-chip">JEF</span><span class="format-chip">PCS</span><span class="format-chip">PES</span><span class="format-chip">SEW</span><span class="format-chip">XIP</span><span class="format-chip">XXX</span></div>
    </div>
    <a class="view-set" href="#"><svg width="12" height="8" viewBox="0 0 12 8"><path d="M0 4C2 0.5 10 0.5 12 4C10 7.5 2 7.5 0 4Z" fill="#fff"/><circle cx="6" cy="4" r="1.8" fill="#b0206c"/></svg>View Set</a>
    <p class="design-card__date">Added/Updated:<br><b>September 20, 2014</b></p>
  </article>
</main>

<p class="pager-status">Page 1 of 84</p>
<a class="pager-next" href="#">Next Page<span>&gt;&gt;</span></a>

<footer class="site-footer">
  <p>Permission granted to use machine embroidery designs for your own commercial and personal embroidery.</p>
  <p>Permission denied to resell or give away machine embroidery designs in electronic format.</p>
</footer>
</body>
</html>
```